Business cards and stationary for a machine shop
K7 Lathe, LLC
Professional
(see below)
48B Garnet Avenue
Natick, MA 01760
dumont@k7lathe-example.com
www.k7lathe-example.com
On the bottom left to be the address, website and phone number
On the bottom right to be both names and cell numbers
Roy Dumont (508)555-0143
Gwen Dumont (508)555-0187
I like the look of this one. I don't know if you can turn it around to be a "P"
This is the AI file of my logo

```html
<!DOCTYPE html>
<html lang="en">
<head>
<meta charset="utf-8">
<title>K7 Lathe, LLC — Stationery Concepts</title>
<link rel="stylesheet" href="https://fonts.googleapis.com/css2?family=Roboto:wght@400;700&display=swap">
<style>
  :root{
    --board-dark:#2c2c2c;
    --board-light:#5a5a5a;
    --paper:#ffffff;
    --ink:#1a1a1a;
    --red:#c4121a;
    --red-deep:#7a0a0e;
    --gray:#9a9a9a;
    --label:#d8d8d8;
    --watermark:#f1f1f1;
  }
  *{box-sizing:border-box;margin:0;padding:0}
  html,body{width:1200px;height:444px;overflow:hidden}
  body{
    position:relative;
    font-family:"Roboto",Arial,sans-serif;
    background:radial-gradient(ellipse at 55% 45%,var(--board-light),var(--board-dark) 80%);
  }
  .piece{position:absolute;box-shadow:0 3px 8px rgba(0,0,0,.55);overflow:hidden}
  .piece svg.art{position:absolute;inset:0;width:100%;height:100%}
  .label{position:absolute;color:var(--label);font-size:8px;text-align:center}
  .wordmark{font-weight:700;color:var(--ink);white-space:nowrap;display:flex;align-items:center;gap:4px}
  .wordmark .dot{width:7px;height:7px;border-radius:50%;background:var(--red)}
  .wordmark.light{color:var(--paper)}

  /* presentation title */
  .title{position:absolute;left:19px;top:150px;width:160px}
  .title .wordmark{font-size:20px;color:var(--paper)}
  .title .wordmark .dot{width:12px;height:12px}
  .title .subtitle{color:var(--label);font-size:11px;margin-top:8px}

  /* business cards */
  .card{left:19px;width:130px;height:76px}
  .card--front{top:236px;background:var(--paper)}
  .card--back{top:346px;background:var(--ink)}
  .card .wordmark{position:absolute;left:8px;top:8px;font-size:9px}
  .card--back .wordmark{top:30px;font-size:11px}
  .card .details{position:absolute;right:6px;bottom:6px;font-size:4px;line-height:1.4;color:var(--paper);text-align:right}

  /* letterheads */
  .letterhead{top:19px;width:276px;height:384px;background:var(--paper)}
  .letterhead--a{left:204px}
  .letterhead--b{left:509px}
  .letterhead .wordmark{position:absolute;left:22px;top:22px;font-size:12px}
  .letterhead .watermark{position:absolute;left:30px;top:90px;font-size:190px;font-weight:700;color:var(--watermark);letter-spacing:-6px}
  .letterhead .contact{position:absolute;font-size:5px;line-height:1.5;color:var(--ink)}
  .letterhead--a .contact{left:160px;top:24px}
  .letterhead--b .contact{right:16px;bottom:14px;color:var(--paper);text-align:right}
  .letterhead .foot{position:absolute;left:16px;bottom:12px;font-size:5px;color:var(--paper)}

  /* envelopes */
  .envelope{left:806px;width:370px;height:94px;background:var(--paper)}
  .envelope--1{top:19px}
  .envelope--2{top:124px;left:816px}
  .envelope--3{top:222px;left:812px}
  .envelope--4{top:312px}
  .envelope .wordmark{position:absolute;font-size:11px}
  .envelope--2 .wordmark{left:155px;top:22px;color:var(--paper)}
  .envelope--3 .wordmark{left:155px;top:20px}
  .envelope--4 .wordmark{left:14px;top:12px}
  .envelope .return{position:absolute;left:14px;top:30px;font-size:5px;line-height:1.5;color:var(--ink)}
</style>
</head>
<body>

<section class="title">
  <div class="wordmark"><span class="dot"></span>K7 Lathe, LLC</div>
  <p class="subtitle">Stationery Concepts</p>
</section>

<!-- business card front -->
<div class="piece card card--front">
  <svg class="art" viewBox="0 0 130 76" preserveAspectRatio="none" aria-hidden="true">
    <path d="M0 34 C40 44 90 40 130 22 V76 H0Z" fill="var(--ink)"/>
    <path d="M0 40 C40 50 90 46 130 30 V40 C90 56 40 60 0 56Z" fill="var(--red)"/>
    <path d="M0 36 C40 46 90 42 130 25" stroke="var(--gray)" stroke-width=".6" fill="none"/>
  </svg>
  <div class="wordmark"><span class="dot"></span>K7 Lathe, LLC</div>
  <div class="details">Roy Dumont (508)555-0143<br>Gwen Dumont (508)555-0187<br>www.k7lathe-example.com</div>
</div>
<p class="label" style="left:19px;top:316px;width:130px">Front Card</p>

<!-- business card back -->
<div class="piece card card--back">
  <svg class="art" viewBox="0 0 130 76" preserveAspectRatio="none" aria-hidden="true">
    <path d="M0 58 C40 66 90 62 130 48 V56 C90 70 40 74 0 70Z" fill="var(--red)"/>
  </svg>
  <div class="wordmark light"><span class="dot"></span>K7 Lathe, LLC</div>
</div>
<p class="label" style="left:19px;top:426px;width:130px">Back Card</p>

<!-- letterhead A -->
<div class="piece letterhead letterhead--a">
  <div class="watermark" aria-hidden="true">K7</div>
  <svg class="art" viewBox="0 0 276 384" preserveAspectRatio="none" aria-hidden="true">
    <path d="M0 0 H276 V4 C190 8 90 14 0 18Z" fill="var(--ink)"/>
    <path d="M0 18 C90 14 190 8 276 4 V8 C190 14 100 24 0 30Z" fill="var(--red)"/>
    <path d="M0 34 C100 28 190 14 276 10" stroke="var(--gray)" stroke-width=".8" fill="none"/>
    <path d="M0 318 C90 346 190 340 276 310 V384 H0Z" fill="var(--red)"/>
    <path d="M0 340 C90 362 190 358 276 332 V384 H0Z" fill="var(--ink)"/>
    <path d="M0 312 C90 340 190 334 276 304" stroke="var(--gray)" stroke-width=".8" fill="none"/>
  </svg>
  <div class="wordmark" style="top:40px"><span class="dot"></span>K7 Lathe, LLC</div>
  <div class="contact">48B Garnet Avenue, Natick, MA 01760<br>dumont@k7lathe-example.com</div>
  <div class="foot">48B Garnet Avenue · Natick, MA 01760 · www.k7lathe-example.com</div>
</div>
<p class="label" style="left:204px;top:418px;width:276px">Letterhead Version A</p>

<!-- letterhead B -->
<div class="piece letterhead letterhead--b">
  <div class="watermark" aria-hidden="true">K7</div>
  <svg class="art" viewBox="0 0 276 384" preserveAspectRatio="none" aria-hidden="true">
    <path d="M0 0 H276 V6 C190 10 90 18 0 22Z" fill="var(--ink)"/>
    <path d="M0 22 C90 18 190 10 276 6 V10 C190 18 100 28 0 34Z" fill="var(--red)"/>
    <path d="M0 38 C100 32 190 18 276 14" stroke="var(--gray)" stroke-width=".8" fill="none"/>
    <path d="M0 322 C90 350 190 344 276 314 V384 H0Z" fill="var(--red)"/>
    <path d="M0 342 C90 364 190 360 276 334 V384 H0Z" fill="var(--ink)"/>
  </svg>
  <div class="wordmark" style="top:44px"><span class="dot"></span>K7 Lathe, LLC</div>
  <div class="foot">48B Garnet Avenue · Natick, MA 01760<br>www.k7lathe-example.com</div>
  <div class="contact">Roy Dumont (508)555-0143<br>Gwen Dumont (508)555-0187</div>
</div>
<p class="label" style="left:509px;top:418px;width:276px">Letterhead Version B</p>

<!-- envelope back, black flap -->
<div class="piece envelope envelope--1">
  <svg class="art" viewBox="0 0 370 94" preserveAspectRatio="none" aria-hidden="true">
    <path d="M0 0 H370 V22 C260 44 110 44 0 22Z" fill="var(--ink)"/>
    <path d="M0 22 C110 44 260 44 370 22" stroke="var(--red)" stroke-width="2" fill="none"/>
  </svg>
</div>

<!-- envelope back, red flap -->
<div class="piece envelope envelope--2">
  <svg class="art" viewBox="0 0 370 94" preserveAspectRatio="none" aria-hidden="true">
    <path d="M0 0 H370 V40 C260 62 110 62 0 40Z" fill="var(--red)"/>
    <path d="M0 40 C110 62 260 62 370 40 V44 C260 66 110 66 0 44Z" fill="var(--red-deep)"/>
    <path d="M0 0 H370 V10 C260 20 110 20 0 10Z" fill="var(--ink)"/>
  </svg>
  <div class="wordmark"><span class="dot" style="background:var(--paper)"></span>K7 Lathe, LLC</div>
</div>

<!-- envelope back, gray flap -->
<div class="piece envelope envelope--3">
  <svg class="art" viewBox="0 0 370 94" preserveAspectRatio="none" aria-hidden="true">
    <defs>
      <linearGradient id="steel" x1="0" x2="1">
        <stop offset="0" stop-color="#6f6f6f"/><stop offset=".5" stop-color="#e8e8e8"/><stop offset="1" stop-color="#6f6f6f"/>
      </linearGradient>
    </defs>
    <path d="M0 0 H370 V36 C260 58 110 58 0 36Z" fill="url(#steel)"/>
  </svg>
  <div class="wordmark"><span class="dot"></span>K7 Lathe, LLC</div>
</div>

<!-- envelope front -->
<div class="piece envelope envelope--4">
  <svg class="art" viewBox="0 0 370 94" preserveAspectRatio="none" aria-hidden="true">
    <path d="M0 70 C120 84 260 80 370 58 V94 H0Z" fill="var(--red)"/>
    <path d="M0 82 C120 94 260 90 370 72 V94 H0Z" fill="var(--ink)"/>
  </svg>
  <div class="wordmark"><span class="dot"></span>K7 Lathe, LLC</div>
  <div class="return">48B Garnet Avenue<br>Natick, MA 01760</div>
</div>
<p class="label" style="left:806px;top:418px;width:370px">Envelope Front &amp; Back</p>

</body>
</html>
```